2-Page Flyer for the Information Session about the Tranquil Venture Course

This is a flyer to announce/advertise an evening Information Session about the Tranquil Venture Course. This Program aims at mindfully rethinking and redesigning work (and life) for people who feel stuck or not entirely satisfied with their work and/or life (please see draft flyer attached for more details). This Program is property of Brightfold Joy, a company that uses a combination of Mindfulness, Design, and Entrepreneurship to help people achieve greater happiness (in their work and lives).
Updates

Target Market(s)

People who feel stuck or not entirely satisfied with their work and/or life (please see draft flyer attached for more details)

Font styles to use
Serif
Sans Serif

Colors
ffffff
f37122
33a6d7
acd037

Requirements
Must have
• All of what I will say below is suggestive (I’m not a design expert), and I’m open to divert from it, if it makes sense and feels more interesting.
• I thought initially of a 2-page flyer (please see draft flyer attached). The first page could help people grasp the essence of the event quickly (in 1 or 2 minutes), and then, if they are interested/motivated, they would continue reading through page 2, which has more info about the Program in itself.
• Potential Structure
• Page 1
• . About the Information Session on the Tranquil Venture Course
• . Visible Date & Time, Contacts, Venue (and other relevant info)
• . About me (the facilitator)
• Page 2
• . About the Tranquil Venture Course
• I include a Powerpoint draft of the flyer with the content. The design is rudimentary and precarious from an aesthetics/organization point of view, and this is mainly where I need help (and maybe in other aspects too!).
• On the flyer, I would like to include:
• . A photo of myself (I attach 1 picture).
• . 1 or 2 beautiful-nature photos (cropped or full). One may have to do with looking at the sky, dreaming, and imagining a new work and life (2 photos with sky and clouds attached). The other has to do with walking the transformation journey (the photo with the person walking through the forest path).
• . brightfold joy logo or logos (there are two slightly different ones, that can be used for different purposes). For the first page, I would like the brightfold joy logo that has "brightfold joy" written on the bottom, with the saying "Stillness, Craft and Venture for Joy" beneath. This is the main logo. For the 2nd page, you can choose the logo that adapts better.
• - Where it says the "the way out is in" it would be great to have a similar font to the one I attach (see file "Font_the_way_out_is_in.png" and Ankecallig-fg.ttf
Nice to have
• In terms of colours, I would not divert much from the logo colours (and of course white and black). I would like the flyer to be quite white. Almost like fairy-tale white: the white horse, the white snow, the white of the stars, the white heaven. White could be the base colour. White means peace, tranquillity, calm contentment, a smile.
• And then use the other colours. The green of the mindfulness. The blue of the sky, the dreams. And the orange of the sun, the energy, the fire, the action. And maybe the black for text.
• Where it says the "the way out is in" it would be great to have a similar font to the one I attach (see file "Font_the_way_out_is_in".
• I would like this flyer to be a piece of art, in every possible way. Simple, beautiful, ease, light, peaceful, calm happy. Just like the Tranquil Venture Course and brightfold joy Company that I am creating intends to be. The mission of this Program and Company is to be a designer, a painter (a Picasso) of happier and more fulfilling human lives.
• I am very much looking forward to seeing your proposal(s).

```html
<!DOCTYPE html>
<html lang="en">
<head>
<meta charset="utf-8">
<title>Tranquil Venture Course – Information Session Flyer</title>
<link href="https://fonts.googleapis.com/css2?family=Source+Sans+3:wght@400;600;700&family=Kaushan+Script&display=swap" rel="stylesheet">
<style>
:root{
  --orange:#ef8430;
  --blue:#3ba6dd;
  --green:#a2c93a;
  --grey:#a7a7a9;
  --ink:#333;
  --dark:#555;
  --white:#fff;
  --stage:#e4e4e4;
}
*{box-sizing:border-box;margin:0;padding:0}
html,body{width:1200px;height:881px;overflow:hidden}
body{background:var(--stage);font-family:"Source Sans 3",Arial,sans-serif;color:var(--ink);position:relative}
.page{position:absolute;top:88px;width:500px;height:706px;background:var(--white);overflow:hidden;box-shadow:0 3px 10px rgba(0,0,0,.25)}
.page--front{left:80px}
.page--back{left:630px}
.abs{position:absolute}
.photo{position:absolute;left:0;top:0;width:500px}
.photo--sky{height:262px;background:linear-gradient(180deg,#8fb3d8 0%,#c7d8e8 30%,#7f93a6 55%,#5f7a52 75%,#486a3a 100%)}
.photo--forest{height:200px;background:linear-gradient(180deg,#3b3526 0%,#6b5a3c 40%,#4c5a2e 75%,#3a4a24 100%)}
.swoosh{position:absolute;left:0;top:0}
.brand{font-weight:400;color:var(--blue);letter-spacing:-.5px;line-height:1}
.brand-mark{position:absolute;border-radius:50%;background:var(--orange)}
.title{position:absolute;left:0;width:500px;top:291px;text-align:center;font-weight:600;font-size:20px;letter-spacing:.4px;color:var(--ink)}
.date-pill{position:absolute;left:104px;top:326px;width:292px;height:26px;border-radius:13px;background:var(--orange);color:var(--white);font-size:13px;text-align:center;line-height:26px;box-shadow:0 2px 3px rgba(0,0,0,.2)}
.col h3{font-size:10.5px;font-weight:700;margin-bottom:2px}
.col p{font-size:8.6px;line-height:1.42;text-align:justify;color:var(--dark)}
.h-blue{color:var(--blue)}
.h-orange{color:var(--orange)}
.facilitator{position:absolute;left:20px;top:468px;width:465px;height:152px;background:var(--orange);border-radius:6px;overflow:hidden;color:var(--white)}
.facilitator__photo{position:absolute;left:28px;top:10px;width:100px;height:142px;background:linear-gradient(180deg,#f3a769 0%,#b7a79a 40%,#34495e 100%);border-radius:4px 4px 0 0}
.facilitator__body{position:absolute;left:138px;top:20px;width:316px}
.facilitator h3{font-size:10.5px;font-weight:700}
.facilitator h4{font-size:8.8px;font-weight:600;margin:2px 0 8px}
.facilitator p{font-size:6.3px;line-height:1.3;font-weight:600}
.facilitator .more{margin-top:8px;font-size:6.3px;font-style:normal;display:flex;align-items:center;gap:5px}
.facilitator .more i{display:inline-block;width:10px;height:10px;border:1px solid var(--white);border-radius:50%}
.booking{position:absolute;left:0;width:500px;top:631px;text-align:center;color:var(--green);font-size:13px}
.venue{position:absolute;left:0;width:500px;top:651px;text-align:center;font-size:8.8px;color:var(--ink)}
.rule{position:absolute;left:0;top:662px;width:500px;height:2px;background:var(--green)}
.footer{position:absolute;left:0;top:669px;width:500px;height:37px;background:var(--grey);display:flex;align-items:center;justify-content:space-around;color:var(--white);font-size:9px}
.footer span{display:flex;align-items:center;gap:4px}
.footer small{font-size:7px}
.quote{position:absolute;left:135px;top:10px;font-family:"Kaushan Script",cursive;font-size:30px;color:var(--white)}
.tab{position:absolute;left:0;top:276px;width:232px;height:22px;background:var(--orange);color:var(--white);font-size:10.5px;font-weight:700;line-height:22px;padding-left:24px;border-radius:0 4px 4px 0;box-shadow:2px 2px 3px rgba(0,0,0,.2)}
.intro{position:absolute;left:24px;top:306px;width:464px;font-size:8.6px;line-height:1.42;color:var(--dark);text-align:justify}
.program{position:absolute;left:22px;top:351px;width:466px;height:128px;background:var(--orange);border-radius:6px;color:var(--white);padding:20px 12px 0}
.program h3{font-size:10.5px;font-weight:700;margin-bottom:12px}
.program p{font-size:8.1px;line-height:1.4;margin-bottom:8px}
.list{list-style:none;margin-top:7px}
.list li{position:relative;padding-left:14px;font-size:8.4px;line-height:1.2;margin-bottom:4px;color:var(--dark)}
.list li::before{content:"›";position:absolute;left:0;top:1px;width:8px;height:8px;border-radius:50%;color:var(--white);font-size:8px;line-height:7px;text-align:center;font-weight:700}
.list--blue li::before{background:var(--blue)}
.list--orange li::before{background:var(--orange)}
.list li.plain::before{display:none}
.back-col p{font-size:8.6px;line-height:1.25;color:var(--dark);text-align:justify}
.back-col h3{font-size:10.5px;font-weight:700}
</style>
</head>
<body>

<section class="page page--front">
  <div class="photo photo--sky" role="img" aria-label="Photograph of green mountain ridges under a wide cloudy sky"></div>
  <svg class="swoosh" width="500" height="300" viewBox="0 0 500 300" aria-hidden="true">
    <path d="M0,290 L0,282 Q240,175 500,245 L500,290 Z" fill="#fff"/>
    <path d="M0,282 Q240,175 500,245" fill="none" stroke="#a2c93a" stroke-width="5"/>
    <path d="M0,289 Q240,184 500,252" fill="none" stroke="#a2c93a" stroke-width="1.2"/>
  </svg>
  <div class="brand-mark" style="left:222px;top:185px;width:56px;height:56px"></div>
  <div class="brand abs" style="left:0;width:500px;top:243px;text-align:center;font-size:28px">brightfold joy</div>

  <h1 class="title">TRANQUIL VENTURE COURSE</h1>
  <div class="date-pill">Thursday 5th September 2019 &nbsp;19:30 to 21:00</div>

  <div class="col abs" style="left:20px;top:380px;width:214px">
    <h3 class="h-blue">INFORMATION SESSION</h3>
    <p>The purpose of this Information Session is to give you a real insight into the Tranquil Venture Course and how it can help you make the most of your professional and personal life.</p>
  </div>
  <div class="col abs" style="left:248px;top:380px;width:238px">
    <h3 class="h-orange">WHO CAN COME</h3>
    <p>The Information Session is free. Whether you come on your own, or with friends or family, you'll be warmly welcome. It will take place on Thursday the 5th September 2019, from 19:30 to 21:00, at Lumen Coworking. Please get in touch for more info or to book a place.</p>
  </div>

  <div class="facilitator">
    <div class="facilitator__photo" role="img" aria-label="Portrait photograph of the facilitator in a dark coat and scarf"></div>
    <div class="facilitator__body">
      <h3>FACILITATOR:</h3>
      <h4>Dr Tomás Varela, Visiting Research Fellow, Northvale University</h4>
      <p>Tomás joined Northvale University as a Lecturer in Entrepreneurship in 2015, after completing his PhD in Entrepreneurship in 2014, which received a national doctoral dissertation award. He began his career as a production engineer and continued in sales. After his MBA, he worked as a strategy consultant. Originally from Portugal, he enjoys designing and launching new ideas, international communities, mindfulness retreats and improvisation. He nurtures a close connection with a mindfulness community. He has practised and volunteered in a mindfulness centre for nine months and shares its benefits with others.</p>
      <div class="more"><i></i>More about the facilitator: profile.northvale.edu/tvarela</div>
    </div>
  </div>

  <div class="booking">Information &amp; Booking</div>
  <div class="venue">Venue: Lumen Coworking, C/ Almendro 12, Barcelona</div>
  <div class="rule"></div>
  <footer class="footer">
    <span><svg width="10" height="10" viewBox="0 0 10 10"><circle cx="5" cy="5" r="5" fill="#a2c93a"/><rect x="2.3" y="3.2" width="5.4" height="3.6" fill="none" stroke="#fff" stroke-width=".8"/><path d="M2.3,3.2 L5,5.2 L7.7,3.2" fill="none" stroke="#fff" stroke-width=".8"/></svg>info@brightfoldjoy.io</span>
    <span><svg width="10" height="10" viewBox="0 0 10 10"><circle cx="5" cy="5" r="5" fill="#a2c93a"/><path d="M3.3,2.6 Q2.6,5.6 6.8,7.3 L7.3,6.2 L6,5.6 L5.5,6.1 Q4.2,5.4 3.9,4.3 L4.4,3.9 L3.9,2.5 Z" fill="#fff"/></svg>+34 611 482 905 <small>(video call and chat)</small></span>
    <span><svg width="10" height="10" viewBox="0 0 10 10"><circle cx="5" cy="5" r="5" fill="#a2c93a"/><circle cx="5" cy="5" r="2.8" fill="none" stroke="#fff" stroke-width=".7"/><path d="M2.2,5 H7.8 M5,2.2 Q3.5,5 5,7.8 M5,2.2 Q6.5,5 5,7.8" fill="none" stroke="#fff" stroke-width=".6"/></svg>brightfoldjoy.io</span>
  </footer>
</section>

<section class="page page--back">
  <div class="photo photo--forest" role="img" aria-label="Photograph of a person walking down a path through a tall pine forest"></div>
  <svg class="swoosh" width="500" height="230" viewBox="0 0 500 230" aria-hidden="true">
    <path d="M0,230 L0,188 Q250,125 500,165 L500,230 Z" fill="#fff"/>
    <path d="M0,188 Q250,125 500,165" fill="none" stroke="#a2c93a" stroke-width="5"/>
    <path d="M0,195 Q250,133 500,172" fill="none" stroke="#a2c93a" stroke-width="1.2"/>
  </svg>
  <div class="quote">“The way out is in”</div>

  <svg class="abs" style="left:230px;top:80px" width="270" height="230" viewBox="0 0 270 230" aria-label="Cycle of four workshops joined by weekly peer support meetings">
    <defs>
      <marker id="arrow" markerWidth="6" markerHeight="6" refX="3" refY="3" orient="auto"><path d="M0,0 L6,3 L0,6" fill="none" stroke="#fff" stroke-width="1"/></marker>
      <marker id="arrowGrey" markerWidth="6" markerHeight="6" refX="3" refY="3" orient="auto"><path d="M0,0 L6,3 L0,6" fill="none" stroke="#bbb" stroke-width="1"/></marker>
    </defs>
    <g font-family="Source Sans 3, Arial, sans-serif" text-anchor="middle" font-weight="700" fill="#333">
      <circle cx="150" cy="44" r="38" fill="#fff"/>
      <path d="M150,6 A38,38 0 0 1 188,44" fill="none" stroke="#ef8430" stroke-width="1.6" stroke-dasharray="4 3"/>
      <text x="150" y="38" font-size="8">Workshop 1</text><text x="150" y="48" font-size="8">INSIGHT</text><text x="150" y="58" font-size="8">(5 hours)</text>
      <circle cx="183" cy="14" r="8" fill="#ef8430"/><text x="183" y="17" font-size="8" fill="#fff" font-weight="400">01</text>

      <circle cx="220" cy="116" r="38" fill="#fff" stroke="#555" stroke-width="1.4" stroke-dasharray="4 3"/>
      <text x="220" y="110" font-size="8">Workshop 2</text><text x="220" y="120" font-size="8">DESIGN</text><text x="220" y="130" font-size="8">(5 hours)</text>
      <circle cx="253" cy="86" r="8" fill="#555"/><text x="253" y="89" font-size="8" fill="#fff" font-weight="400">02</text>

      <circle cx="150" cy="183" r="38" fill="#fff" stroke="#a2c93a" stroke-width="1.4" stroke-dasharray="4 3"/>
      <text x="150" y="177" font-size="8">Workshop 3</text><text x="150" y="187" font-size="8">EXECUTE</text><text x="150" y="197" font-size="8">(5 hours)</text>
      <circle cx="183" cy="153" r="8" fill="#a2c93a"/><text x="183" y="156" font-size="8" fill="#fff" font-weight="400">03</text>

      <circle cx="77" cy="116" r="38" fill="#fff" stroke="#3ba6dd" stroke-width="1.4" stroke-dasharray="4 3"/>
      <text x="77" y="110" font-size="8">Workshop 4</text><text x="77" y="120" font-size="8">PRESENT</text><text x="77" y="130" font-size="8">(5 hours)</text>
      <circle cx="110" cy="86" r="8" fill="#3ba6dd"/><text x="110" y="89" font-size="8" fill="#fff" font-weight="400">04</text>

      <path d="M203,57 Q214,62 218,72" fill="none" stroke="#fff" stroke-width="1.6" marker-end="url(#arrow)"/>
      <path d="M230,165 Q222,175 210,178" fill="none" stroke="#bbb" stroke-width="1.6" marker-end="url(#arrowGrey)"/>
      <path d="M95,176 Q86,168 83,160" fill="none" stroke="#bbb" stroke-width="1.6" marker-end="url(#arrowGrey)"/>
      <path d="M84,68 Q90,56 100,50" fill="none" stroke="#fff" stroke-width="1.6" marker-end="url(#arrow)"/>

      <g font-size="5.4" font-weight="400" fill="#fff">
        <text x="236" y="12">Weekly Peer Support</text><text x="236" y="19">(WPS) meetings</text><text x="236" y="26">(2 hours)</text>
        <text x="40" y="40">WPS meetings</text>
      </g>
      <g font-size="5.4" font-weight="400" fill="#555">
        <text x="246" y="196">WPS meetings</text>
        <text x="32" y="195">WPS meetings</text>
      </g>
    </g>
  </svg>

  <div class="brand-mark" style="left:26px;top:205px;width:48px;height:48px"></div>
  <div class="brand abs" style="left:100px;top:195px;font-size:27px;color:var(--orange);line-height:.95">brightfold<br>joy</div>

  <div class="tab">What is Tranquil Venture?</div>
  <p class="intro">Being mindful means being aware and awake. Entrepreneurship is the creation of a new form of organising. Tranquil Venture is then the process of creating or redesigning your work and life with awareness, in a way that is reflective of you, of your passions and values, thus conducting to a greater sense of fulfilment and happiness.</p>

  <div class="program">
    <h3>THE PROGRAM</h3>
    <p>The Tranquil Venture Course is a 4-month long transformative journey designed for people who feel stuck or not entirely satisfied with their professional and/or personal life. It will be of benefit for everyone, at any stage.</p>
    <p>The Program consists of a 5-hour workshop every month, complemented by 2-hour weekly peer support meetings. It combines mindfulness techniques, design thinking methodology, and entrepreneurship frameworks.</p>
  </div>

  <div class="back-col abs" style="left:24px;top:496px;width:222px">
    <h3 class="h-blue">WHY</h3>
    <p>Many people are not satisfied with their work or life, but they don't know what to do about it. This Program offers you a safe place to conduct your inner journey with collective support, helping you reflect, design, and (very likely) do something about it. It aims at:</p>
    <ul class="list list--blue">
      <li>Increasing awareness, clarity and confidence</li>
      <li>Having a deeper insight on what makes you happier and what you want</li>
      <li>Developing a clear design integrating your intended work and life</li>
      <li>Start executing this design</li>
    </ul>
  </div>
  <div class="back-col abs" style="left:258px;top:496px;width:230px">
    <h3 class="h-orange">HOW</h3>
    <p>This Program differs from existing entrepreneurial programs in many ways:</p>
    <ul class="list list--orange">
      <li>Uses mindfulness and self analysis to look deeply into yourself</li>
      <li>Design and execution decisions are based on happiness rather than (only) financials</li>
      <li class="plain">Holistic and inclusive design process, integrating work and life, and building synergies between your different parts.</li>
    </ul>
    <p style="margin-top:6px">The Program format includes lectures, individual work, group sharing, guided activities, experiential exercises, video, audio, handouts and other resources.</p>
  </div>

  <div class="rule"></div>
  <footer class="footer">
    <span><svg width="10" height="10" viewBox="0 0 10 10"><circle cx="5" cy="5" r="5" fill="#a2c93a"/><rect x="2.3" y="3.2" width="5.4" height="3.6" fill="none" stroke="#fff" stroke-width=".8"/><path d="M2.3,3.2 L5,5.2 L7.7,3.2" fill="none" stroke="#fff" stroke-width=".8"/></svg>info@brightfoldjoy.io</span>
    <span><svg width="10" height="10" viewBox="0 0 10 10"><circle cx="5" cy="5" r="5" fill="#a2c93a"/><path d="M3.3,2.6 Q2.6,5.6 6.8,7.3 L7.3,6.2 L6,5.6 L5.5,6.1 Q4.2,5.4 3.9,4.3 L4.4,3.9 L3.9,2.5 Z" fill="#fff"/></svg>+34 611 482 905 <small>(video call and chat)</small></span>
    <span><svg width="10" height="10" viewBox="0 0 10 10"><circle cx="5" cy="5" r="5" fill="#a2c93a"/><circle cx="5" cy="5" r="2.8" fill="none" stroke="#fff" stroke-width=".7"/><path d="M2.2,5 H7.8 M5,2.2 Q3.5,5 5,7.8 M5,2.2 Q6.5,5 5,7.8" fill="none" stroke="#fff" stroke-width=".6"/></svg>brightfoldjoy.io</span>
  </footer>
</section>

</body>
</html>
```